KW Orbena Agency

we need a design for panel, cm 235 x 184 height + roll up as attached sizes, attached find also my logo, my company is www.kworbenaagency.com

Freight Forwarding

```html
<!DOCTYPE html>
<html lang="en">
<head>
<meta charset="utf-8">
<title>KW Orbena Agency – Roll-up Banner</title>
<link rel="stylesheet" href="https://fonts.googleapis.com/css2?family=Oswald:wght@700&family=Saira+Condensed:wght@600&family=Arimo&family=Montserrat+Alternates:ital,wght@1,800&display=swap">
<style>
:root{
  --navy:#1f2358;
  --red:#d4201f;
  --grey-text:#555a62;
  --label:#5a5e66;
  --page:#eef2f8;
  --panel-light:#f4f5f7;
  --panel-mid:#e1e3e8;
}
*{margin:0;padding:0;box-sizing:border-box}
html,body{width:1200px;height:1200px;overflow:hidden;background:var(--page)}
.banner{
  position:absolute;left:357px;top:30px;width:486px;height:1140px;overflow:hidden;
  background:linear-gradient(160deg,var(--panel-light) 0%,var(--panel-mid) 45%,var(--panel-light) 70%,var(--panel-mid) 100%);
  box-shadow:0 4px 14px rgba(0,0,0,.25);
}
.banner > *{position:absolute}
.hero-photo{left:0;top:0;width:486px;height:370px;
  background:linear-gradient(180deg,#6f9cc9 0%,#a9c6e2 35%,#dbe6f0 60%,#c9b9ae 82%,#e8ecf1 100%)}
.swoosh{left:0;top:345px;width:486px;height:40px}
.brand-mark{left:0;width:486px;top:58px;text-align:center;font-family:'Oswald',sans-serif;font-weight:700;font-size:26px;color:var(--navy);letter-spacing:2px;display:flex;justify-content:center;align-items:center;gap:10px}
.brand-mark .dot{width:22px;height:22px;border-radius:50%;background:var(--red)}
.company{left:0;width:486px;top:112px;text-align:center;font-family:'Oswald',sans-serif;font-weight:700;font-size:42px;line-height:50px;color:var(--navy);transform:scaleX(.88)}
.tagline{left:0;width:486px;top:160px;text-align:center;font-family:'Saira Condensed',sans-serif;font-weight:600;font-size:28px;color:var(--red);letter-spacing:1px}
.headline{left:0;width:486px;top:396px;text-align:center;font-family:'Oswald',sans-serif;font-weight:700;font-size:40px;line-height:48px;color:var(--red);transform:scaleX(.9)}
.intro{left:40px;width:406px;top:510px;text-align:center;font-family:'Arimo',sans-serif;font-size:12.5px;line-height:14.6px;color:var(--grey-text)}
.service{width:220px;text-align:center}
.service svg{display:block;margin:0 auto}
.service h3{font-family:'Montserrat Alternates',sans-serif;font-style:italic;font-weight:800;font-size:23px;line-height:27px;color:var(--label)}
.col-left{left:22px}.col-right{left:255px}
.row-1{top:626px}.row-2{top:792px}
.contact{left:0;width:486px;top:952px;text-align:center}
.contact svg{display:block;margin:0 auto}
.phone{font-family:'Oswald',sans-serif;font-weight:700;font-size:34px;line-height:40px;color:var(--navy)}
.handle{font-family:'Montserrat Alternates',sans-serif;font-style:italic;font-weight:800;font-size:14px;line-height:18px;color:var(--navy)}
.footer{left:0;top:1040px;width:486px;height:100px}
.footer-text{left:0;width:486px;top:1064px;text-align:center}
.cta{font-family:'Montserrat Alternates',sans-serif;font-style:italic;font-weight:800;font-size:23px;line-height:26px;color:#8b8d96}
.url{font-family:'Oswald',sans-serif;font-weight:700;font-size:29px;line-height:36px;color:#fff;display:inline-block;transform:scaleX(.9)}
</style>
</head>
<body>
<main class="banner">
  <div class="hero-photo" role="img" aria-label="Sky over a port with container ship, freight train, cargo plane, forklift and truck carrying containers"></div>
  <svg class="swoosh" viewBox="0 0 486 40" preserveAspectRatio="none">
    <path d="M0 14 Q200 -4 470 10 Q220 6 0 38 Z" fill="var(--red)"/>
    <path d="M0 38 Q220 6 470 10 L486 10 L486 40 L0 40 Z" fill="var(--panel-light)"/>
  </svg>
  <div class="brand-mark"><span class="dot"></span>KW ORBENA</div>
  <h1 class="company">KW ORBENA AGENCY</h1>
  <p class="tagline">Shipping and Logistics</p>
  <h2 class="headline">WE MAKE YOUR BUSINESS<br>FLOW CONTINOUSLY</h2>
  <p class="intro">KW Orbena Agency has an understanding that your business<br>is our first priority.<br>As a result, we deliver outstanding services to fuel growth,<br>Expand operations, and deliver measurable<br>results to the highest expectations.<br>Allow KW Orbena Agency to take your shipping<br>Services to the next level!</p>

  <section class="service col-left row-1">
    <svg width="80" height="70" viewBox="0 0 80 70" fill="none" stroke="var(--red)" stroke-width="3" stroke-linejoin="round">
      <path d="M6 18 L34 6 L58 16 L30 28 Z"/><path d="M6 18 V42 L30 54 V28"/><path d="M58 16 V28"/>
      <path d="M18 13 L44 24"/>
      <g transform="translate(38 26) rotate(45 17 17) scale(1.45)" stroke-width="2">
        <path d="M21 16v-2l-8-5V3.5c0-.83-.67-1.5-1.5-1.5S10 2.67 10 3.5V9l-8 5v2l8-2.5V19l-2 1.5V22l3.5-1 3.5 1v-1.5L13 19v-5.5l8 2.5z"/>
      </g>
    </svg>
    <h3>Freight<br>Forwarding</h3>
  </section>
  <section class="service col-right row-1">
    <svg width="76" height="66" viewBox="0 0 76 66" fill="none" stroke="var(--red)" stroke-width="3" stroke-linejoin="round">
      <path d="M4 22 L38 4 L72 22 V64 H4 Z"/><rect x="14" y="26" width="48" height="38"/>
      <rect x="30" y="10" width="16" height="4"/><rect x="40" y="44" width="12" height="10"/><rect x="32" y="54" width="12" height="10"/><rect x="46" y="54" width="12" height="10"/>
    </svg>
    <h3>Warehouse<br>Logistics</h3>
  </section>
  <section class="service col-left row-2">
    <svg width="80" height="74" viewBox="0 0 80 74" fill="none" stroke="var(--red)" stroke-width="3" stroke-linejoin="round" stroke-linecap="round">
      <path d="M18 12 L52 4 L66 10 V38 L32 46 L18 40 Z"/><path d="M18 12 L32 18 L66 10"/><path d="M32 18 V46"/>
      <path d="M40 8 L52 13 V20"/>
      <rect x="2" y="54" width="8" height="18"/>
      <path d="M10 57 H26 Q32 57 36 60 H50 Q55 60 55 64 Q55 67 50 67 H36"/>
      <path d="M10 70 H46 Q54 70 66 62 Q74 58 75 62 Q75 65 68 69 Q58 74 46 74 H10"/>
    </svg>
    <h3>Project<br>Cargoes</h3>
  </section>
  <section class="service col-right row-2">
    <svg width="104" height="74" viewBox="0 0 104 74" fill="none" stroke="var(--red)" stroke-width="3" stroke-linejoin="round">
      <rect x="2" y="26" width="28" height="28"/><rect x="34" y="26" width="28" height="28"/><path d="M66 34 H88 L100 44 V54 H66 Z"/>
      <path d="M8 34 H24 M40 34 H56 M74 42 H86"/>
      <circle cx="10" cy="60" r="4"/><circle cx="24" cy="60" r="4"/><circle cx="42" cy="60" r="4"/><circle cx="56" cy="60" r="4"/><circle cx="76" cy="60" r="4"/><circle cx="92" cy="60" r="4"/>
    </svg>
    <h3>Rail<br>Services</h3>
  </section>

  <div class="contact">
    <svg width="18" height="16" viewBox="0 0 24 24"><path d="M6.6 10.8a15 15 0 0 0 6.6 6.6l2.2-2.2a1 1 0 0 1 1-.25 11.4 11.4 0 0 0 3.6.6 1 1 0 0 1 1 1V20a1 1 0 0 1-1 1A17 17 0 0 1 3 4a1 1 0 0 1 1-1h3.5a1 1 0 0 1 1 1c0 1.25.2 2.45.6 3.6a1 1 0 0 1-.25 1z" fill="var(--red)"/></svg>
    <p class="phone">+39 0288150376</p>
    <p class="handle">@kworbenaagency.com</p>
  </div>

  <svg class="footer" viewBox="0 0 486 100" preserveAspectRatio="none">
    <path d="M0 6 Q243 26 486 2 V100 H0 Z" fill="var(--navy)"/>
  </svg>
  <div class="footer-text">
    <p class="cta">choose us!</p>
    <span class="url">www.kworbenaagency.com</span>
  </div>
</main>
</body>
</html>
```